Small dedicated blog website

I have recently had a logo designed for my growing personal hobby, I document my adventures around the world in video form (www.vidplenta.com/harrowmeadtrips.com) I am now trying to create a small blog website with easy access to my other social networks to start to create a home base for all the videos and content I create, I would like a simple website with a focus on blog posts and access to my other social networks, pictoloom (harrowmeadtrips), palverse (harrowmeadtrips), blinkpost (kelvinharrowmead)

My current website can be viewed at www.harrowmeadtrips.com

Please contact me for any further information to help this project

Many thanks!

I do not expect a fully coded website, simply designs and graphics

Industry/Entity Type

Social

Font styles to use
Sans Serif

Requirements
Must have
• area for quillo blog placement, access to social media links

```html
<!DOCTYPE html>
<html lang="en">
<head>
<meta charset="utf-8">
<title>harrowmeadtrips – My first apartment</title>
<link href="https://fonts.googleapis.com/css2?family=Montserrat:wght@400;700&family=Playfair+Display:wght@400&family=Crimson+Text:ital,wght@0,400;1,400&display=swap" rel="stylesheet">
<style>
:root{
  --accent:#e85c5f;
  --ink:#2b2b2b;
  --body:#4a4a4a;
  --muted:#a6a6a6;
  --line:#e6e6e6;
  --band:#e8e8e8;
  --card:#ffffff;
  --foot:#f4f4f4;
}
*{box-sizing:border-box;margin:0;padding:0}
html,body{width:726px;height:1200px;overflow:hidden;background:#fff}
body{position:relative;font-family:"Crimson Text",Georgia,serif;color:var(--body)}
.abs{position:absolute}
/* header */
.brand{left:0;width:726px;top:28px;text-align:center}
.brand-mark{display:block;width:22px;height:22px;border-radius:50%;background:var(--ink);margin:0 auto 10px}
.brand-name{font-family:"Montserrat",Arial,sans-serif;font-weight:700;font-size:8.5px;letter-spacing:.8px;color:var(--ink)}
.header-rule{left:48px;width:630px;top:94px;border-top:1px solid var(--line)}
.main-nav{left:0;width:726px;top:115px;text-align:center;font-size:10.5px;letter-spacing:.2px}
.main-nav a{color:var(--ink);text-decoration:none;padding:0 6px;border-left:1px solid #ddd}
.main-nav a:first-child{border-left:0}
.main-nav a.current{color:var(--accent)}
/* band */
.content-band{left:0;top:139px;width:726px;height:874px;background:var(--band)}
.card{background:var(--card);box-shadow:0 1px 2px rgba(0,0,0,.08)}
.post{left:48px;top:149px;width:415px;height:802px}
.post-icon{left:383px;top:20px;width:14px;height:18px;border:1.5px solid #d4d4d4;border-radius:2px}
.post-title{left:32px;top:32px;font-family:"Playfair Display",Georgia,serif;font-size:22px;color:var(--ink);font-weight:400}
.post-meta{left:32px;top:68px;font-size:7.5px;color:var(--muted)}
.photo{background:linear-gradient(135deg,#d9d6cf,#8d8a84)}
.photo-kitchen{left:31px;top:86px;width:162px;height:144px;background:linear-gradient(160deg,#f2f2f0,#9a948c)}
.photo-living{left:193px;top:86px;width:189px;height:144px;background:linear-gradient(160deg,#e9e7e3,#6d6760)}
.photo-building{left:31px;top:230px;width:351px;height:189px;background:linear-gradient(180deg,#c4cfdc 0%,#e4d9a8 45%,#bdb9ad 80%,#e9ecef 100%)}
.post-body{left:31px;top:440px;width:352px;font-size:11.6px;line-height:16.6px;text-align:justify}
.drop{float:left;font-size:44px;line-height:38px;margin:2px 6px 0 0;font-family:"Playfair Display",Georgia,serif;color:var(--ink)}
.post-body p.tail{text-align:left}
.read-more{left:0;width:415px;top:704px;text-align:center;font-style:italic;font-size:11px;color:var(--accent)}
.post-rule{left:31px;width:352px;top:730px;border-top:1px dashed var(--line)}
.share{left:0;width:415px;top:756px;display:flex;justify-content:center;gap:5px}
.share span{width:23px;height:23px;border:1px solid #ddd;border-radius:50%;display:flex;align-items:center;justify-content:center}
.older{left:48px;top:981px;font-style:italic;font-size:11px;color:var(--accent)}
/* sidebar */
.widget-title{font-size:11.5px;color:var(--ink);letter-spacing:.2px;padding-bottom:8px;border-bottom:1px solid var(--line);width:142px}
.about{left:479px;top:149px;width:199px;height:371px}
.about .widget-title{position:absolute;left:29px;top:39px}
.avatar{left:28px;top:67px;width:143px;height:170px;border:3px solid #222;background:linear-gradient(150deg,#d8c9b4,#b48f74 60%,#3e3a36)}
.about-text{left:30px;top:263px;width:150px;font-size:11.3px;line-height:14px;color:var(--ink)}
.socials{left:479px;top:537px;width:199px;height:92px;display:flex;justify-content:center;align-items:center;gap:7px}
.socials a{display:flex;flex-direction:column;align-items:center;gap:3px;text-decoration:none;color:var(--accent);font-size:7.5px}
.socials i{display:block;width:13px;height:13px;background:var(--accent)}
.archive{left:479px;top:648px;width:199px;height:225px}
.archive .widget-title{position:absolute;left:29px;top:39px}
.archive ul{position:absolute;left:29px;top:70px;list-style:none;font-size:11.3px;line-height:16.2px}
.archive a{color:var(--accent);text-decoration:none}
/* footer */
.quote{left:78px;width:570px;top:1050px;text-align:center;font-style:italic;font-size:10.5px;color:#777}
.quote b{position:absolute;font-family:"Playfair Display",serif;font-style:normal;font-size:34px;color:#ccc;font-weight:400}
.foot-brand{left:0;width:726px;top:1090px;text-align:center}
.foot-brand .brand-mark{background:#cfcfcf;width:26px;height:26px;margin-bottom:14px}
.foot-brand .brand-name{color:#d0d0d0;font-size:8px}
.bottom-bar{left:0;top:1166px;width:726px;height:34px;background:var(--foot);font-size:7.5px;color:#777}
.bottom-bar nav{position:absolute;left:56px;top:13px}
.bottom-bar nav a{color:#555;text-decoration:none}
.bottom-bar nav em{color:#ccc;font-style:normal;margin:0 5px}
.copy{position:absolute;right:46px;top:13px;color:#999}
.to-top{position:absolute;right:4px;top:3px;width:28px;height:28px;background:#fff}
</style>
</head>
<body>
<header>
  <div class="abs brand"><span class="brand-mark"></span><span class="brand-name">HARROWMEADTRIPS.COM</span></div>
  <div class="abs header-rule"></div>
  <nav class="abs main-nav"><a class="current" href="#">HOME</a><a href="#">CATEGORIES</a><a href="#">COUNTRIES</a><a href="#">ABOUT ME</a><a href="#">CONTACT</a><a href="#">GALLERY</a></nav>
</header>

<div class="abs content-band"></div>

<article class="abs card post">
  <div class="abs post-icon"></div>
  <h1 class="abs post-title">My first apartment</h1>
  <div class="abs post-meta">By admin / Friday, January 3, 2014 / 1 / Life / Permalink / ♡ 20</div>
  <div class="abs photo-kitchen" role="img" aria-label="Photo of the white apartment kitchen"></div>
  <div class="abs photo-living" role="img" aria-label="Photo of the living room with sofa and window"></div>
  <div class="abs photo-building" role="img" aria-label="Photo of the yellow apartment building in snow"></div>
  <div class="abs post-body">
    <p><span class="drop">I</span> signed a one year lease on my first apartment! It feels extremely surreal and with the same motion a sigh of relief. Prior to signing this lease I had a one way ticket to a place I've been dreaming of for years to study environmental engineering, but I've had this little knot in my stomach knowing I had no place yet to call home, of course I've applied for student housing but nothing was coming through and with my approaching departure I started to look elsewhere. A dear Finnish friend of mine, Liisa helped me with searching for properties as my Finnish is still limited! Liisa found me a perfect studio apartment on the top floor of a one year old complex and within 24 hours I had signed a lease and paid deposits. I'm thrilled! It has put the excitement back into this new journey I'm going on, 46 days and counting :)</p>
    <p class="tail">But who has any right to find fault with a man who chooses to enjoy a pleasure that has no annoying consequences, or one who avoids a pain that produces no resultant pleasure?</p>
  </div>
  <div class="abs read-more">Continue Reading...</div>
  <div class="abs post-rule"></div>
  <div class="abs share" aria-label="Share this post">
    <span></span><span></span><span></span><span></span><span></span><span></span><span></span><span></span><span></span>
    <span><svg width="10" height="8" viewBox="0 0 10 8"><rect x=".5" y=".5" width="9" height="7" fill="none" stroke="#bbb"/><path d="M.5 .5L5 4.5L9.5 .5" fill="none" stroke="#bbb"/></svg></span>
  </div>
</article>

<aside>
  <section class="abs card about">
    <h2 class="widget-title">ABOUT ME</h2>
    <div class="abs avatar" role="img" aria-label="Portrait of the blogger wearing sunglasses"></div>
    <p class="abs about-text">I'm a tri-citizen of our beautiful planet and this is my diary of my various adventures recent relocation to Finland.</p>
  </section>
  <section class="abs card socials">
    <a href="#"><i></i>Palverse</a>
    <a href="#"><i></i>Chirpline</a>
    <a href="#"><i></i>Orbitplus</a>
    <a href="#"><i></i>Pictoloom</a>
  </section>
  <section class="abs card archive">
    <h2 class="widget-title">SEARCH THE ARCHIVES</h2>
    <ul>
      <li><a href="#">January 2014</a></li><li><a href="#">December 2013</a></li><li><a href="#">September 2013</a></li><li><a href="#">August 2013</a></li><li><a href="#">June 2013</a></li><li><a href="#">May 2013</a></li><li><a href="#">April 2013</a></li><li><a href="#">January 2013</a></li>
    </ul>
  </section>
</aside>

<a class="abs older">« Older Entries</a>

<footer>
  <div class="abs quote"><b style="left:0;top:-14px">“</b>I'm a tri-citizen of our beautiful planet and this is my diary of my various adventures recent relocation to Finland.<b style="right:0;top:-6px">”</b></div>
  <div class="abs foot-brand"><span class="brand-mark"></span><span class="brand-name">HARROWMEADTRIPS.COM</span></div>
  <div class="abs bottom-bar">
    <nav><a href="#">Home</a><em>/</em><a href="#">About me</a><em>/</em><a href="#">Gallery</a><em>/</em><a href="#">Contact</a></nav>
    <span class="copy">Copyrights © 2014. All Rights Reserved.</span>
    <span class="to-top"><svg width="28" height="28" viewBox="0 0 28 28"><path d="M8 17L14 11L20 17" fill="none" stroke="#ccc" stroke-width="1.2"/></svg></span>
  </div>
</footer>
</body>
</html>
```